Rambler K7 Side Vinyls on BLACK

This is a 2 sided wrap for a Rambler K7 with no door handles and blacked out windows. It's for an In-Home Care Service called Willowgate Care. I will upload the design elements we'd like to see with the text to be used with our Logo. The text we need is: 865-555-0147 - There is no place like home - A Safe and Secure Alternative to Nursing Home Care - Willowgate Care - That with faces of patient and caregiver will probably fill up the space. I would like to see a swirly graphical treatment in our two PMS colors Blue = 2935C Green = 376C. Attached find art pic of Rambler to go by and artwork with logo. The brochure art is just to let you know the feel of our brand. Thanks and please let me know if you have any questions. To clarify, the Rambler is BLACK.
Updates

I'm sorry but the RAMBLER is gone and we will be getting a TORVIK PEBBLE today for the vinyl decals.  I will be choosing a design in the next few days but here's some feedback.  We are looking for vinyl decals not a full vinyl wrap.  We would like the faces on the image to go over the black window in the back.  In other words, use the entire back, not just up to the window line.  We are looking for some nice design elements, swirls, etc. and the wording with phone number and website address.  If anyone wants to resubmit with this update, I'd appreciate it, but if you don't, I understand that as well and we'll pick from the existing designs.  I appreciate all of the hard work everyone has done on this project and hope to use all of you in the near future.

Doran Pettigrew
Willowgate Care

Pebble iswhite

Target Market(s)

Baby Boomers and Older

Industry/Entity Type

Nursing Home

Requirements
Must have
• Vibrant colors

```html
<!DOCTYPE html>
<html lang="en">
<head>
<meta charset="utf-8">
<title>Willowgate Care – Side Decals</title>
<link href="https://fonts.googleapis.com/css2?family=Questrial&family=Roboto:wght@500;700&display=swap" rel="stylesheet">
<style>
  :root {
    --brand-blue: #0057b8;
    --brand-blue-deep: #1b3f8f;
    --brand-green: #84bd00;
    --panel-mid: #d9dbde;
    --canvas-bg: #ffffff;
  }
  html, body {
    margin: 0;
    padding: 0;
    width: 1200px;
    height: 900px;
    overflow: hidden;
    background: var(--canvas-bg);
  }
  .decal-sheet { display: block; width: 1200px; height: 900px; }
  .slogan { font-family: "Roboto", sans-serif; font-weight: 500; font-size: 22px; }
  .slogan-blue { fill: var(--brand-blue-deep); }
  .slogan-green { fill: var(--brand-green); }
  .tagline { font-family: "Roboto", sans-serif; font-weight: 500; font-size: 11.5px; fill: var(--brand-green); }
  .phone { font-family: "Roboto", sans-serif; font-weight: 700; font-size: 37px; fill: var(--brand-blue-deep); }
  .brand-name { font-family: "Questrial", sans-serif; font-size: 42px; fill: #ffffff; }
  .brand-dot { fill: var(--brand-green); }
  .band-blue { fill: var(--brand-blue); }
  .band-green { fill: var(--brand-green); }
  .panel-base { fill: url(#panelShade); }
  .slogan-box { fill: var(--panel-mid); }
</style>
</head>
<body>
<svg class="decal-sheet" viewBox="0 0 1200 900" xmlns="http://www.w3.org/2000/svg">
  <defs>
    <linearGradient id="panelShade" x1="0" y1="0" x2="0" y2="1">
      <stop offset="0" stop-color="#f6f7f8"/>
      <stop offset="1" stop-color="#dfe1e4"/>
    </linearGradient>
    <linearGradient id="photoRight" x1="0" y1="0" x2="1" y2="0">
      <stop offset="0" stop-color="#eef1f3"/>
      <stop offset="0.55" stop-color="#e3d6c9"/>
      <stop offset="1" stop-color="#c9a88e"/>
    </linearGradient>
    <linearGradient id="photoLeft" x1="1" y1="0" x2="0" y2="0">
      <stop offset="0" stop-color="#eef1f3"/>
      <stop offset="0.55" stop-color="#e3d6c9"/>
      <stop offset="1" stop-color="#c9a88e"/>
    </linearGradient>
  </defs>

  <g class="decal decal-driver-side">
    <rect class="panel-base" x="290" y="55" width="655" height="265" rx="14"/>
    <g role="img" aria-label="Photo of a smiling caregiver and an elderly man">
      <rect x="728" y="58" width="214" height="130" rx="6" fill="url(#photoRight)"/>
    </g>
    <rect class="slogan-box" x="545" y="60" width="162" height="86" rx="8"/>
    <text class="slogan slogan-blue" x="562" y="88">There is</text>
    <text class="slogan slogan-green" x="585" y="113">no place</text>
    <text class="slogan slogan-blue" x="585" y="136">like home</text>

    <path class="band-green" d="M290 262 C430 262 520 250 620 222 C730 192 840 182 945 180 L945 190 C840 192 735 204 625 234 C525 260 430 272 290 272 Z"/>
    <path class="band-blue" d="M290 272 C430 272 525 260 625 234 C735 204 840 192 945 190 L945 306 Q945 320 931 320 L304 320 Q290 320 290 306 Z"/>

    <text class="tagline" transform="translate(540 198) rotate(-7)">A Safe and Secure Alternative to Nursing Home Care</text>
    <text class="phone" transform="translate(538 234) rotate(-7)">865-555-0147</text>

    <circle class="brand-dot" cx="425" cy="228" r="20"/>
    <text class="brand-name" x="345" y="302">Willowgate Care</text>
  </g>

  <g class="decal decal-passenger-side">
    <rect class="panel-base" x="288" y="478" width="660" height="268" rx="14"/>
    <g role="img" aria-label="Photo of an elderly man and a smiling caregiver">
      <rect x="291" y="481" width="212" height="132" rx="6" fill="url(#photoLeft)"/>
    </g>
    <rect class="slogan-box" x="538" y="500" width="150" height="86" rx="8"/>
    <text class="slogan slogan-blue" x="553" y="527">There is</text>
    <text class="slogan slogan-green" x="573" y="552">no place</text>
    <text class="slogan slogan-blue" x="573" y="575">like home</text>

    <path class="band-green" d="M288 610 C400 612 510 626 610 654 C720 684 830 700 948 700 L948 710 C830 710 720 694 605 664 C505 638 400 622 288 620 Z"/>
    <path class="band-blue" d="M288 620 C400 622 505 638 605 664 C720 694 830 710 948 710 L948 732 Q948 746 934 746 L302 746 Q288 746 288 732 Z"/>

    <text class="tagline" transform="translate(452 574) rotate(15)">A Safe and Secure Alternative to Nursing Home Care</text>
    <text class="phone" transform="translate(440 608) rotate(15)">865-555-0147</text>

    <circle class="brand-dot" cx="812" cy="650" r="20"/>
    <text class="brand-name" x="562" y="728">Willowgate Care</text>
  </g>
</svg>
</body>
</html>
```